Stationary/Web Page
Project: Business Cards
Business Cards
Professional
Joel Varrick
President
4817 W. Pelham Ridge Dunmore Rd. Baytown, TX 77409
JoelVarrick_OTW@mailbrook.com

```html
<!DOCTYPE html>
<html lang="en">
<head>
<meta charset="utf-8">
<title>Harlow Finch Fitouts – Stationery Set</title>
<link href="https://fonts.googleapis.com/css2?family=Open+Sans:wght@400;600;700;800&display=swap" rel="stylesheet">
<style>
  :root{
    --stage:#e4e5e7;
    --paper:#ffffff;
    --paper-shade:#f1f1f2;
    --red:#c8161d;
    --red-bright:#e3272d;
    --red-deep:#5e0609;
    --ink:#3a3a3c;
    --ink-soft:#8a8b8e;
    --rule:#d7d7d9;
    --ghost:#ececed;
  }
  *{box-sizing:border-box;margin:0;padding:0}
  html,body{width:1200px;height:641px;overflow:hidden}
  body{background:var(--stage);font-family:"Open Sans",Arial,sans-serif;color:var(--ink);position:relative}
  .piece{position:absolute;background:var(--paper);box-shadow:0 2px 6px rgba(0,0,0,.22);overflow:hidden}
  .band{position:absolute;left:0;width:100%}
  .brand{position:absolute;font-weight:700;color:var(--red);white-space:nowrap;line-height:1}
  .seal{position:absolute;border-radius:50%;background:var(--red)}
  .ghost-disc{position:absolute;border-radius:50%;background:var(--ghost)}
  .small{font-size:4px;color:var(--ink-soft);line-height:1.45;position:absolute}
  .address-light{color:#f3d0d1;text-align:right}
  .set-label{position:absolute;left:48px;font-size:5px;font-weight:600;color:#6b6c6f}

  /* business cards */
  .card{width:173px;height:98px;left:48px}
  .card-front .brand{left:11px;top:14px;font-size:8px}
  .card-front .contact{left:11px;top:34px}
  .card-front .name-tag{position:absolute;left:11px;top:70px;background:var(--red);color:#fff;padding:3px 7px;font-size:5px;font-weight:700;border-radius:2px;line-height:1.2}
  .card-front .name-tag span{display:block;font-size:3.5px;font-weight:400}
  .card-back{background:radial-gradient(circle at 50% 50%,var(--red) 0%,var(--red-deep) 75%)}
  .card-back .seal{width:46px;height:46px;left:63px;top:26px;background:var(--red-bright)}

  /* letterhead */
  .letterhead{left:252px;top:24px;width:408px;height:600px}
  .letterhead .brand{left:20px;top:60px;font-size:10px}
  .letterhead .contact{right:14px;top:8px}
  .letterhead .ghost-disc{width:124px;height:124px;left:118px;top:166px}
  .letterhead .seal{width:46px;height:46px;right:30px;bottom:20px}

  /* fax */
  .fax{left:684px;top:24px;width:425px;height:600px}
  .fax .brand{left:20px;top:64px;font-size:9px}
  .fax .contact{right:14px;top:8px}
  .fax-title{position:absolute;left:20px;top:84px;font-size:24px;font-weight:800;color:var(--red);line-height:1}
  .fax-fields{position:absolute;left:20px;top:138px;width:385px;display:grid;grid-template-columns:1fr 1fr;column-gap:24px;row-gap:5px}
  .fax-field{display:flex;align-items:center;gap:4px;height:11px}
  .fax-field b{background:var(--red);color:#fff;font-size:4.5px;font-weight:600;width:38px;height:11px;line-height:11px;padding-left:4px}
  .fax-field i{flex:1;border-bottom:1px solid var(--rule);height:11px}
  .fax-checks{position:absolute;left:66px;top:218px;display:flex;gap:24px}
  .fax-checks span{display:flex;align-items:center;gap:3px;font-size:4px;color:var(--ink-soft)}
  .fax-checks span::before{content:"";width:5px;height:5px;border:1px solid var(--ink-soft)}
  .fax .ghost-disc{width:124px;height:124px;left:150px;top:226px}
  .fax .seal{width:48px;height:48px;right:50px;bottom:40px}

  /* window envelope */
  .envelope-window{left:307px;top:312px;width:413px;height:211px}
  .envelope-window .brand{left:22px;top:46px;font-size:9px}
  .envelope-window .return{left:22px;top:112px}
  .envelope-window .window{position:absolute;left:14px;top:180px;width:92px;height:24px;border:1px solid var(--rule);background:var(--paper-shade);border-radius:3px}
  .envelope-window .flap-seal{position:absolute;left:199px;top:6px;width:12px;height:12px;border-radius:50%;background:var(--red-bright)}
  .envelope-window .seal{width:44px;height:44px;right:30px;top:154px}

  /* plain envelope */
  .envelope-plain{left:749px;top:329px;width:415px;height:223px}
  .envelope-plain .brand{left:20px;top:30px;font-size:9px}
  .envelope-plain .return{left:20px;top:56px}
  .envelope-plain .seal{width:44px;height:44px;right:30px;top:128px}
</style>
</head>
<body>

<defs-holder>
<svg width="0" height="0" style="position:absolute" aria-hidden="true">
  <defs>
    <linearGradient id="cardRed" x1="0" y1="0" x2="1" y2="0"><stop offset="0" stop-color="#8e0c10"/><stop offset="1" stop-color="#d31b21"/></linearGradient>
    <linearGradient id="bandRed" x1="0" y1="0" x2="1" y2="0"><stop offset="0" stop-color="#4e0507"/><stop offset=".55" stop-color="#a5111a"/><stop offset="1" stop-color="#d41d24"/></linearGradient>
  </defs>
</svg>
</defs-holder>

<!-- business cards -->
<div class="set-label" style="top:43px">Business Card Elevated</div>
<article class="piece card card-front" style="top:60px">
  <svg class="band" style="top:0" width="173" height="98" viewBox="0 0 173 98" aria-hidden="true">
    <path d="M112 0H173V98C150 66 130 34 112 0Z" fill="url(#cardRed)"/>
    <path d="M98 0C124 40 146 70 173 98" stroke="#e9b3b5" stroke-width="1" fill="none"/>
  </svg>
  <p class="brand">Harlow Finch Fitouts</p>
  <p class="contact small">4817 W. Pelham Ridge Dunmore Rd.<br>Baytown, TX 77409<br>JoelVarrick_OTW@mailbrook.com</p>
  <p class="name-tag">Joel Varrick<span>President</span></p>
</article>
<article class="piece card card-back" style="top:182px"><span class="seal"></span></article>

<div class="set-label" style="top:346px">Business Card Standard</div>
<article class="piece card card-front" style="top:364px">
  <svg class="band" style="top:0" width="173" height="98" viewBox="0 0 173 98" aria-hidden="true">
    <path d="M112 0H173V98C150 66 130 34 112 0Z" fill="url(#cardRed)"/>
  </svg>
  <p class="brand">Harlow Finch Fitouts</p>
  <p class="contact small">4817 W. Pelham Ridge Dunmore Rd.<br>Baytown, TX 77409<br>JoelVarrick_OTW@mailbrook.com</p>
  <p class="name-tag">Joel Varrick<span>President</span></p>
</article>
<article class="piece card card-back" style="top:481px"><span class="seal"></span></article>

<!-- letterhead -->
<article class="piece letterhead">
  <svg class="band" style="top:0" width="408" height="56" viewBox="0 0 408 56" preserveAspectRatio="none" aria-hidden="true">
    <path d="M0 0H408V26C280 30 140 52 0 40Z" fill="url(#bandRed)"/>
    <path d="M0 46C140 58 280 36 408 32" stroke="#cfcfd1" stroke-width="1" fill="none"/>
  </svg>
  <p class="contact small address-light">4817 W. Pelham Ridge Dunmore Rd.<br>Baytown, TX 77409<br>Ph: 281.555.0142</p>
  <p class="brand">Harlow Finch Fitouts</p>
  <span class="ghost-disc"></span>
  <svg class="band" style="bottom:0" width="408" height="70" viewBox="0 0 408 70" preserveAspectRatio="none" aria-hidden="true">
    <path d="M0 70V40C140 20 280 30 408 10V70Z" fill="url(#bandRed)"/>
  </svg>
  <span class="seal"></span>
</article>

<!-- fax sheet -->
<article class="piece fax">
  <svg class="band" style="top:0" width="425" height="56" viewBox="0 0 425 56" preserveAspectRatio="none" aria-hidden="true">
    <path d="M0 0H425V26C290 30 150 52 0 40Z" fill="url(#bandRed)"/>
    <path d="M0 46C150 58 290 36 425 32" stroke="#cfcfd1" stroke-width="1" fill="none"/>
  </svg>
  <p class="contact small address-light">4817 W. Pelham Ridge Dunmore Rd.<br>Baytown, TX 77409<br>Ph: 281.555.0142</p>
  <p class="brand">Harlow Finch Fitouts</p>
  <p class="fax-title">FAX</p>
  <div class="fax-fields">
    <div class="fax-field"><b>To</b><i></i></div><div class="fax-field"><b>From</b><i></i></div>
    <div class="fax-field"><b>Fax</b><i></i></div><div class="fax-field"><b>Pages</b><i></i></div>
    <div class="fax-field"><b>Phone</b><i></i></div><div class="fax-field"><b>Date</b><i></i></div>
    <div class="fax-field"><b>Re</b><i></i></div><div class="fax-field"><b>CC</b><i></i></div>
  </div>
  <div class="fax-checks">
    <span>Urgent</span><span>For Review</span><span>Please Comment</span><span>Please Reply</span><span>Please Recycle</span>
  </div>
  <span class="ghost-disc"></span>
  <svg class="band" style="bottom:0" width="425" height="70" viewBox="0 0 425 70" preserveAspectRatio="none" aria-hidden="true">
    <path d="M0 70V40C150 20 290 30 425 10V70Z" fill="url(#bandRed)"/>
  </svg>
  <span class="seal"></span>
</article>

<!-- window envelope -->
<article class="piece envelope-window">
  <svg class="band" style="top:0" width="413" height="44" viewBox="0 0 413 44" preserveAspectRatio="none" aria-hidden="true">
    <path d="M0 0H413V24C280 18 220 44 0 36Z" fill="url(#bandRed)"/>
    <path d="M0 40C220 48 280 24 413 30" stroke="#cfcfd1" stroke-width="1" fill="none"/>
  </svg>
  <span class="flap-seal"></span>
  <p class="brand">Harlow Finch Fitouts</p>
  <p class="return small">4817 W. Pelham Ridge Dunmore Rd.<br>Baytown, TX 77409</p>
  <span class="window"></span>
  <svg class="band" style="bottom:0" width="413" height="46" viewBox="0 0 413 46" preserveAspectRatio="none" aria-hidden="true">
    <path d="M0 46V30C140 14 270 30 413 4V46Z" fill="url(#bandRed)"/>
  </svg>
  <span class="seal"></span>
</article>

<!-- plain envelope -->
<article class="piece envelope-plain">
  <p class="brand">Harlow Finch Fitouts</p>
  <p class="return small">4817 W. Pelham Ridge Dunmore Rd.<br>Baytown, TX 77409</p>
  <svg class="band" style="bottom:0" width="415" height="66" viewBox="0 0 415 66" preserveAspectRatio="none" aria-hidden="true">
    <path d="M0 66V36C150 16 280 40 415 8V66Z" fill="url(#bandRed)"/>
    <path d="M0 28C150 8 280 32 415 0" stroke="#cfcfd1" stroke-width="1" fill="none"/>
  </svg>
  <span class="seal"></span>
</article>

</body>
</html>
```